KRV Business Cards

We are a local commercial development company based in Silicon Valley and we would like a new business card. I've attached a copy of our company brochure to give a flavor of what we do, our logo, info company colors/graphics, and our current business card. We don't necessarily need a crazy makeover, but would like something that feels a little bit more "fresh" and modern (we've had the same business card design for 15+ years), but still in keeping with our overall brand -- clean, high-quality, modern but timeless. Would like to add our website to the info on the card (www.velmara.com) and would like the flexibility for some folks to have an efax number listed and some not to have that included (without it looking like there is a hole).

```html
<!DOCTYPE html>
<html lang="en">
<head>
<meta charset="utf-8">
<title>KRV Business Card</title>
<link href="https://fonts.googleapis.com/css2?family=Cinzel:wght@400&family=Crimson+Pro:ital,wght@1,400&display=swap" rel="stylesheet">
<style>
  :root {
    --navy: #2e4a66;
    --navy-deep: #2a4560;
    --teal: #4e7880;
    --teal-soft: #7fa7b0;
    --ink-light: #e3eaee;
    --paper: #ffffff;
    --backdrop: #e9ebed;
  }
  html, body {
    margin: 0; padding: 0;
    width: 1200px; height: 1200px;
    overflow: hidden;
    background: var(--backdrop);
  }
  .canvas { position: relative; width: 1200px; height: 1200px; }
  .card {
    position: absolute; left: 175px;
    width: 850px; height: 472px;
    overflow: hidden;
    box-shadow: 0 6px 18px rgba(30, 45, 60, 0.25);
  }
  /* Front side */
  .card-front {
    top: 110px;
    background: linear-gradient(100deg, var(--navy-deep) 0%, var(--navy) 45%, var(--teal) 100%);
  }
  .front-name {
    position: absolute; left: 0; right: 0; top: 200px;
    text-align: center;
    font-family: "Cinzel", serif; font-size: 32px; line-height: 38px;
    color: rgba(127, 167, 176, 0.45);
    letter-spacing: 1px;
    white-space: nowrap;
  }
  .front-rule { position: absolute; left: 0; width: 100%; height: 3px; background: rgba(127, 167, 176, 0.35); }
  .front-rule.upper { top: 341px; }
  .front-rule.lower { top: 354px; }
  .front-tagline {
    position: absolute; left: 0; right: 0; top: 368px; margin: 0;
    text-align: center;
    font-family: "Crimson Pro", serif; font-style: italic;
    font-size: 19px; line-height: 23px;
    color: var(--teal-soft);
  }
  /* Back side */
  .card-back { top: 620px; background: var(--paper); }
  .company-name {
    position: absolute; left: 14px; top: 60px; width: 230px;
    display: flex; align-items: center; justify-content: center; gap: 9px;
  }
  .company-mark { width: 12px; height: 12px; background: var(--navy); flex: none; }
  .company-text {
    font-family: "Cinzel", serif; font-size: 20px; line-height: 24px;
    color: var(--navy); white-space: nowrap;
  }
  .company-tagline {
    position: absolute; left: 14px; width: 230px; top: 150px; margin: 0;
    text-align: center;
    font-family: "Crimson Pro", serif; font-style: italic;
    font-size: 16px; line-height: 20px; color: var(--navy);
  }
  .person-name {
    position: absolute; left: 273px; top: 46px;
    font-family: "Cinzel", serif; font-size: 42px; line-height: 48px;
    color: var(--navy); letter-spacing: 1px; white-space: nowrap;
  }
  .person-title {
    position: absolute; right: 163px; top: 82px;
    font-family: "Crimson Pro", serif; font-style: italic;
    font-size: 24px; line-height: 28px; color: var(--navy);
  }
  .accent-swoosh { position: absolute; left: 253px; top: 120px; }
  .web-band {
    position: absolute; left: 321px; right: 0; top: 202px; height: 50px;
    background: linear-gradient(90deg, rgba(78,120,128,0) 0%, rgba(78,120,128,0.7) 30%, var(--teal) 55%, var(--navy) 100%);
  }
  .web-address {
    position: absolute; right: 14px; top: 1px;
    font-family: "Crimson Pro", serif; font-style: italic;
    font-size: 40px; line-height: 46px; color: var(--paper);
    letter-spacing: 1px; white-space: nowrap;
  }
  .contact-band {
    position: absolute; left: 0; right: 0; bottom: 0; height: 132px;
    background: linear-gradient(100deg, var(--navy) 0%, var(--teal) 100%);
  }
  .contact-list {
    position: absolute; left: 27px; top: 15px; margin: 0; padding: 0; list-style: none;
    font-family: "Crimson Pro", serif; font-style: italic;
    font-size: 19px; line-height: 23px; color: var(--ink-light);
  }
  .contact-list .gap { margin-left: 14px; }
</style>
</head>
<body>
<div class="canvas">
  <section class="card card-front" aria-label="Card front">
    <div class="front-name">KRV DEVELOPMENT</div>
    <div class="front-rule upper"></div>
    <div class="front-rule lower"></div>
    <p class="front-tagline">Excellence in<br>Commercial Development</p>
  </section>

  <section class="card card-back" aria-label="Card back">
    <div class="company-name">
      <span class="company-mark"></span>
      <span class="company-text">KRV DEVELOPMENT</span>
    </div>
    <p class="company-tagline">Excellence in<br>Commercial Development</p>

    <div class="person-name">DANA L. WHITCOMB</div>
    <div class="person-title">Partner</div>

    <svg class="accent-swoosh" width="590" height="16" viewBox="0 0 590 16" aria-hidden="true">
      <defs>
        <linearGradient id="swooshFade" x1="0" y1="0" x2="1" y2="0">
          <stop offset="0" stop-color="#4e7880" stop-opacity="0"/>
          <stop offset="0.6" stop-color="#4e7880"/>
          <stop offset="1" stop-color="#2e4a66"/>
        </linearGradient>
      </defs>
      <polygon points="0,0 590,0 545,16 0,16" fill="url(#swooshFade)"/>
    </svg>

    <div class="web-band"><span class="web-address">www.velmara.com</span></div>

    <div class="contact-band">
      <ul class="contact-list">
        <li>318 Harbor Lane, Menlo Park, California 94025</li>
        <li>direct 650.555.0148<span class="gap">main 650.555.0100</span></li>
        <li>fax 650.555.0192</li>
        <li>email: dana@velmara.com</li>
      </ul>
    </div>
  </section>
</div>
</body>
</html>
```